依頼詳細
載内容詳細に関しては、別添のExcel資料を参照してください。

・ターゲット
BtoB
マンションの管理組合や管理業者
BtoC
防水工事系の仕事経験者の方で仕事を探している方

・カラーイメージ
青系
ロゴで使用されている青色を使用して、デザインお願いします。
▼参考
https://www.harumizu-cycle.jp/

・デザイン、ムード
参考のように企業らしい堅めのイメージでデザインお願いします
▼参考
http://www.tomonaga-kiko.biz
https://www.seiran-kenchi.co.jp/

配置やデザイン等はアレンジしていただいて構いません。
また、縦に制限はありません。

レスポンシブデザインのサイトで、bootstrap4を利用しコーディングする予定になります。

デザイン幅は2000px、コンテンツの幅はbootstrap4デフォルトのの1110pxを基準としてください。
ただし、最近のデザインの流行を取りいれて、フルワイドや、1200~1500px程度の幅のコンテンツをバランスよくレイアウトしてください。
コンテンツ配置は基本12分割になります。がデザインによっては、多少逸脱してもかまいません。
bootstrap4、12分割グリッドの基準のPSDも資料として添付しております。
ご参考になさってください。

本分のフォントはゴシック系は游ゴシック、メイリオ、明朝系は遊明朝でお願いします。
飾り文字はフリーフォントか、googleフォントを利用してください。

メイン画像部分・グローバルメニューは、ワイド適用でお願いします。

不明点、質問などありましたらメッセージ等でご連絡ください。
サイトURL
ページ数
1ページ
希望イメージ
シンプル 複雑
単色 カラフル
暗い 明るい
日常 高級
遊び心 厳粛
未来的 伝統的
女性的 男性的
希望する色
青系、水色系
納品ファイル
• 高解像度JPG (.jpg)
• フォトショップ形式 (.psd)
補足説明
・資料上はサイト名(社名)や住所などは伏字にしております。
ご提案時点ではそのまま作成をお願いします。

・使用画像は当選後こちらで用意します。
ご提案時点では前項同様に、カンプデータ等をご使用のうえ、当選後に本内容へ差し替え修正をお願いします。
また、雰囲気が合っていれば、指定外の画像を追加掲載いただいてOKです。

・当選前提となった方は正式な社名及び連絡先をお伝えしますので修正対応をお願いします。

お客様が希望されていたデザインイメージにピッタリだったため。

数多くの素晴らしい提案をいただきありがとうございました。
また次回もご参加よろしくお願いいたします。

```html
<!DOCTYPE html>
<html lang="ja">
<head>
<meta charset="utf-8">
<title>株式会社〇〇〇〇</title>
<link href="https://fonts.googleapis.com/css2?family=Cormorant+Garamond:wght@500;600&family=Noto+Sans+JP:wght@400;500;700&family=Noto+Serif+JP:wght@500;600;700&display=swap" rel="stylesheet">
<style>
:root{
  --navy:#1b3576;
  --blue:#2a56a6;
  --sky:#5f8fd0;
  --pale:#eaf1fa;
  --ghost:#dfe7f3;
  --ink:#1f2633;
  --grey:#6b7280;
  --white:#fff;
}
*{margin:0;padding:0;box-sizing:border-box}
html,body{width:1200px;height:2724px;overflow:hidden;background:var(--white)}
body{font-family:"Noto Sans JP",sans-serif;color:var(--ink);position:relative}
.serif{font-family:"Noto Serif JP",serif}
.abs{position:absolute}

/* header */
.site-header{position:absolute;left:0;top:0;width:1200px;height:68px;background:var(--white);z-index:5;display:flex;align-items:center}
.brand{display:flex;align-items:center;gap:10px;margin-left:22px;font-weight:700;font-size:17px;color:var(--navy)}
.brand-dot{width:26px;height:26px;border-radius:50%;background:var(--blue)}
.gnav{display:flex;margin-left:auto;height:68px}
.gnav a{display:flex;align-items:center;padding:0 22px;font-size:13px;color:var(--ink);text-decoration:none;border-left:1px solid #e3e7ee}
.gnav a.current{color:var(--blue);font-weight:700}
.tel{width:200px;height:68px;background:var(--navy);color:var(--white);display:flex;align-items:center;justify-content:center;gap:10px;font-size:22px;font-weight:700;letter-spacing:.04em}

/* hero */
.hero-photo{left:180px;top:68px;width:1020px;height:560px;background:linear-gradient(180deg,#9fc2e8 0%,#cfe0f1 45%,#b9c9a8 80%,#8fa877 100%)}
.hero-band{left:0;top:200px;width:180px;height:428px;background:linear-gradient(180deg,#ffffff,#e8eff8)}
.hero-title{left:48px;top:368px;font-family:"Cormorant Garamond",serif;font-weight:600;font-size:70px;line-height:1.05;letter-spacing:.06em;color:var(--white);text-shadow:0 2px 10px rgba(20,40,90,.35)}
.hero-title span{color:var(--navy);text-shadow:none}
.hero-sub{left:28px;top:584px;padding:10px 22px;background:var(--navy);color:var(--white);font-size:22px;letter-spacing:.08em}

/* ghost words */
.ghost{font-family:"Cormorant Garamond",serif;font-weight:500;color:var(--ghost);letter-spacing:.06em;line-height:1}

/* section heading */
.sec-title{font-family:"Noto Serif JP",serif;font-weight:600;font-size:26px;color:var(--ink);letter-spacing:.1em;text-align:center}
.sec-title::after{content:"";display:block;width:40px;height:2px;background:var(--blue);margin:12px auto 0}

/* about */
.about-text{left:300px;top:840px;width:600px;font-size:14px;line-height:2;text-align:center;color:#3a4252}
.skyline{left:0;top:920px;width:1200px;height:150px;background:linear-gradient(180deg,rgba(255,255,255,0) 0%,#dce7f5 55%,#c5d7ee 100%)}

/* business */
.business{left:0;top:1080px;width:1200px;height:440px;background:var(--pale)}
.cards{left:30px;top:1262px;width:1140px;display:flex;gap:12px}
.card{position:relative;flex:1;height:176px;background:linear-gradient(135deg,#33548f,#1b3576);display:flex;align-items:center;justify-content:center;color:var(--white);font-family:"Noto Serif JP",serif;font-size:28px;letter-spacing:.12em}
.card .frame{position:absolute;inset:22px}

/* works */
.works{left:0;top:1728px;width:1200px;display:grid;grid-template-columns:repeat(3,1fr);gap:10px}
.work{height:300px}
.btn{left:440px;top:2386px;width:320px;height:46px;background:var(--navy);color:var(--white);font-size:13px;letter-spacing:.2em;display:flex;align-items:center;justify-content:center}

/* recruit */
.recruit{left:260px;top:2466px;width:680px;height:120px;background:linear-gradient(90deg,#1b3576 0%,#2a56a6 45%,#8fb4e2 100%);padding:24px 36px;color:var(--white)}
.recruit h3{font-family:"Noto Serif JP",serif;font-size:22px;letter-spacing:.1em;margin-bottom:8px}
.recruit p{font-size:12px;line-height:1.7;width:460px}

/* footer */
.footer{left:0;top:2600px;width:1200px;height:100px;background:#f2f4f7;border-top:1px solid #e3e6eb}
.f-brand{left:150px;top:2622px}
.f-info{left:150px;top:2660px;font-size:10px;line-height:1.6;color:var(--grey)}
.f-links{left:660px;top:2622px;display:grid;grid-template-columns:160px 160px;row-gap:6px;font-size:11px;color:#444}
.f-links span::before{content:"";display:inline-block;width:5px;height:5px;background:var(--blue);margin-right:8px;vertical-align:middle}
.copy{left:0;top:2700px;width:1200px;height:24px;background:var(--navy);color:var(--white);font-size:10px;display:flex;align-items:center;justify-content:center;letter-spacing:.08em}
</style>
</head>
<body>

<header class="site-header">
  <div class="brand"><span class="brand-dot"></span>株式会社〇〇〇〇</div>
  <nav class="gnav">
    <a class="current">HOME</a><a>業務内容</a><a>施工事例</a><a>会社概要</a><a>お問い合わせ</a>
  </nav>
  <div class="tel">
    <svg width="20" height="20" viewBox="0 0 24 24" fill="#fff"><path d="M6.6 10.8a15 15 0 0 0 6.6 6.6l2.2-2.2a1 1 0 0 1 1-.25 11.4 11.4 0 0 0 3.6.6 1 1 0 0 1 1 1V20a1 1 0 0 1-1 1A17 17 0 0 1 3 4a1 1 0 0 1 1-1h3.5a1 1 0 0 1 1 1c0 1.25.2 2.45.6 3.6a1 1 0 0 1-.25 1z"/></svg>
    000-000-0000
  </div>
</header>

<div class="abs hero-band"></div>
<div class="abs hero-photo" role="img" aria-label="マンションを背景に手をつないで歩く家族の写真"></div>
<h1 class="abs hero-title">SAFE AND<br>SECURE LIFE</h1>
<p class="abs hero-sub serif">安心安全の生活を当たり前にするためのお手伝い</p>

<div class="abs ghost" style="left:120px;top:680px;font-size:120px">ABOUT US</div>
<h2 class="abs sec-title" style="left:0;top:776px;width:1200px">わたしたちについて</h2>
<p class="abs about-text">〇〇〇〇は、大規模修繕工事を中心に<br>防水工事・外壁補修工事・塗装工事を手がけてまいりました。<br>地域の皆様の安心で快適な暮らしを支え続けます。</p>
<div class="abs skyline" role="img" aria-label="淡い青のビル街のイラスト"></div>

<section class="abs business"></section>
<div class="abs ghost" style="left:740px;top:1120px;font-size:120px;color:#d3deee">BUSINESS</div>
<h2 class="abs sec-title" style="left:0;top:1182px;width:1200px">業務内容</h2>
<div class="abs cards">
  <div class="card" role="img" aria-label="防水工事の施工写真"><svg class="frame" viewBox="0 0 100 100" preserveAspectRatio="none"><path d="M0 25V0h14M86 100h14V75" fill="none" stroke="#fff" stroke-width="1.2" vector-effect="non-scaling-stroke"/></svg>防水工事</div>
  <div class="card" role="img" aria-label="外壁補修工事の施工写真"><svg class="frame" viewBox="0 0 100 100" preserveAspectRatio="none"><path d="M0 25V0h14M86 100h14V75" fill="none" stroke="#fff" stroke-width="1.2" vector-effect="non-scaling-stroke"/></svg>外壁補修工事</div>
  <div class="card" role="img" aria-label="外壁塗装の足場写真"><svg class="frame" viewBox="0 0 100 100" preserveAspectRatio="none"><path d="M0 25V0h14M86 100h14V75" fill="none" stroke="#fff" stroke-width="1.2" vector-effect="non-scaling-stroke"/></svg>外壁塗装</div>
</div>

<div class="abs ghost" style="left:440px;top:1540px;font-size:120px">CASE</div>
<h2 class="abs sec-title" style="left:0;top:1666px;width:1200px">施工事例</h2>
<div class="abs works">
  <div class="work" role="img" aria-label="白とグレーの戸建住宅の施工事例" style="background:linear-gradient(180deg,#8fb7e6,#d9dde3 60%,#8a8f96)"></div>
  <div class="work" role="img" aria-label="ベージュの戸建住宅の施工事例" style="background:linear-gradient(180deg,#a9c8ec,#d8c9b0 60%,#9a8f80)"></div>
  <div class="work" role="img" aria-label="石張り外壁の住宅の施工事例" style="background:linear-gradient(180deg,#9fbfe6,#c7bba8 55%,#7d766c)"></div>
  <div class="work" role="img" aria-label="白い外壁の戸建住宅の施工事例" style="background:linear-gradient(180deg,#b5d0ef,#eceae6 55%,#a9a7a2)"></div>
  <div class="work" role="img" aria-label="木目ドアの住宅玄関の施工事例" style="background:linear-gradient(180deg,#c0d6ee,#e6ddd0 55%,#b69a7c)"></div>
  <div class="work" role="img" aria-label="黄色い外壁の住宅の施工事例" style="background:linear-gradient(180deg,#7fa6dd,#e6cf8a 55%,#8c7d5c)"></div>
</div>
<div class="abs btn">VIEW MORE</div>

<div class="abs recruit" role="img" aria-label="青い背景の採用情報バナー">
  <h3>採用情報</h3>
  <p>〇〇〇〇では、経験を活かして一緒に働ける仲間を募集しています。<br>未経験の方もお気軽にご応募ください。</p>
</div>
<div class="abs ghost" style="left:700px;top:2528px;font-size:80px;color:#c9d7ec">RECRUIT</div>

<footer class="abs footer"></footer>
<div class="abs f-brand brand" style="margin:0">
  <span class="brand-dot"></span>株式会社〇〇〇〇
</div>
<p class="abs f-info">〒000-0000 〇〇県〇〇市〇〇町0-0-0<br>TEL 000-000-0000 / FAX 000-000-0000</p>
<div class="abs f-links">
  <span>HOME</span><span>会社概要</span>
  <span>業務内容</span><span>採用情報</span>
  <span>施工事例</span><span>お問い合わせ</span>
</div>
<div class="abs copy">© 株式会社〇〇〇〇 All Rights Reserved.</div>

</body>
</html>
```